Events Online Video Streaming Company

A website needs to be designed to replace the current website of a company that specialises in providing an online portal for streaming events to users. the current portal exists at: http://www.qulmora.com <- designers can get a "feel" for what they do and the content they require from this existing website.
the current qulmora logo and green color are to be maintined. i will upload an EPS of the logo soon.
The new design needs to highlight the main aspects of what they do: live streaming of events, multiple cameras, online chat, user activity data (like zintro dashtrack), customised front-ends.
we want the design to be in-between a corporate feel and modern, contemporary. ie. we dont want it to be too corporate (like the current website).
the design must also incorporate the word: glimmerfolk as part of their slogan or sub-title.
hi everyone,

```html
<!DOCTYPE html>
<html lang="en">
<head>
<meta charset="utf-8">
<title>qulmora — Social Digital Portal</title>
<link rel="stylesheet" href="https://fonts.googleapis.com/css2?family=Arimo:wght@400;700&family=Poppins:wght@200;300&display=swap">
<style>
  :root {
    --green: #8dc63f;
    --green-bar: #7cb82f;
    --green-light: #a8ec4c;
    --green-dark: #1d5a0e;
    --ink: #111111;
    --text: #333333;
    --muted: #666666;
    --band-grey: #b3b3b3;
    --footer-grey: #505050;
    --footer-dark: #262626;
    --edu: #17b8ef;
    --comms: #7a45ad;
    --gig: #e2005a;
  }
  * { box-sizing: border-box; margin: 0; padding: 0; }
  html, body { width: 1079px; height: 1200px; overflow: hidden; background: #fff; }
  body { position: relative; font-family: "Arimo", Arial, sans-serif; color: var(--text); }
  .abs { position: absolute; white-space: nowrap; }
  .wrap { white-space: normal; }

  .site-header { left: 0; top: 0; width: 1079px; height: 82px;
    background: linear-gradient(to bottom, var(--green-light), #5ea52a 45%, var(--green-dark)); }
  .brand-box { left: 107px; top: 14px; width: 236px; height: 68px; background: #fff; }
  .brand-name { left: 136px; top: 18px; font-size: 40px; line-height: 44px; color: var(--green); letter-spacing: -1px; }
  .brand-slogan { left: 138px; top: 64px; font-size: 11px; line-height: 12px; color: var(--muted); letter-spacing: 0.5px; }
  .main-nav a { position: absolute; top: 38px; color: #fff; text-decoration: none; font-size: 17.5px; }

  .pillar { top: 127px; font-family: "Poppins", sans-serif; font-weight: 200; font-size: 56px; color: var(--ink); line-height: 1; letter-spacing: -1px; }
  .pillar-dot { width: 9px; height: 9px; border-radius: 50%; background: var(--green); top: 161px; }

  .band { left: 0; top: 236px; width: 1079px; height: 80px; background: var(--band-grey); }
  .band-highlight { left: 107px; top: 219px; width: 283px; height: 97px; }

  .welcome { left: 142px; top: 360px; font-size: 32px; font-weight: 700; color: var(--green); }
  .tagline { left: 141px; top: 398px; font-family: "Poppins", sans-serif; font-weight: 200; font-size: 27px; color: var(--ink); letter-spacing: -0.5px; }

  .feature-bar { top: 481px; height: 44px; background: var(--green-bar); color: #fff; font-weight: 700; font-size: 17px; line-height: 44px; padding-left: 42px; }
  .feature-num { top: 473px; width: 60px; height: 60px; border-radius: 50%; background: #1a1a1a; color: #fff; font-weight: 700; font-size: 19px; text-align: center; line-height: 60px; }
  .feature-text { top: 547px; font-size: 13.7px; line-height: 16.4px; color: var(--text); }

  .divider { left: 160px; top: 723px; width: 754px; height: 2px;
    background: linear-gradient(to right, rgba(170,170,170,0), #aaa 20%, #aaa 80%, rgba(170,170,170,0)); }

  .badge { top: 783px; height: 46px; border-radius: 3px; color: #fff; font-weight: 700; font-size: 30px; line-height: 46px; text-align: center; }
  .badge-edu { left: 136px; width: 150px; background: var(--edu); }
  .badge-sport { left: 343px; width: 150px; background: linear-gradient(to bottom, #8fdc3c, #1e6410); }
  .badge-comms { left: 549px; width: 184px; background: var(--comms); }
  .badge-gig { left: 788px; width: 150px; background: var(--gig); }
  .category-title { top: 842px; font-family: "Arimo", Arial, sans-serif; font-size: 22px; color: #333; }
  .category-text { top: 871px; font-size: 12px; line-height: 14.6px; color: #333; }

  .footer-links { left: 0; top: 965px; width: 1079px; height: 162px; background: var(--footer-grey); }
  .footer-col { top: 995px; color: #fff; }
  .footer-col h3 { font-size: 13.5px; font-weight: 700; margin-bottom: 14px; }
  .footer-col li { list-style: none; font-size: 12px; line-height: 23px; }

  .footer-bar { left: 0; top: 1127px; width: 1079px; height: 73px; background: var(--footer-dark); }
  .footer-brand { left: 149px; top: 1142px; font-size: 31px; color: #9a9a9a; letter-spacing: -0.5px; }
  .footer-nav a { position: absolute; top: 1160px; color: #bdbdbd; text-decoration: none; font-size: 12.5px; }
  .social-square { top: 1147px; width: 33px; height: 33px; background: linear-gradient(to bottom, #8fdc3c, #1e6410);
    color: #fff; font-weight: 700; font-size: 18px; line-height: 33px; text-align: center; text-decoration: none; }
</style>
</head>
<body>
  <header>
    <div class="abs site-header"></div>
    <div class="abs brand-box"></div>
    <div class="abs brand-name">qulmora</div>
    <div class="abs brand-slogan">live events for glimmerfolk</div>
    <nav class="main-nav">
      <a href="#" style="left:380px">HOME</a>
      <a href="#" style="left:461px">FEATURES</a>
      <a href="#" style="left:579px">APPS</a>
      <a href="#" style="left:658px">TEAM</a>
      <a href="#" style="left:734px">SUPPORT</a>
      <a href="#" style="left:845px">CONTACT</a>
    </nav>
  </header>

  <section class="pillars">
    <span class="abs pillar-dot" style="left:143px"></span>
    <div class="abs pillar" style="left:162px">SOCIAL</div>
    <span class="abs pillar-dot" style="left:434px"></span>
    <div class="abs pillar" style="left:453px">DIGITAL</div>
    <span class="abs pillar-dot" style="left:719px"></span>
    <div class="abs pillar" style="left:737px">PORTAL</div>
  </section>

  <div class="abs band"></div>
  <svg class="abs band-highlight" viewBox="0 0 283 97" aria-hidden="true">
    <defs>
      <linearGradient id="bandGreen" x1="0" x2="1" y1="0" y2="0">
        <stop offset="0" stop-color="#0e5306"/>
        <stop offset="1" stop-color="#b7f75a"/>
      </linearGradient>
    </defs>
    <path d="M0 17 H115 L141 0 L167 17 H283 V97 H0 Z" fill="url(#bandGreen)"/>
  </svg>

  <h1 class="abs welcome">Welcome to qulmora</h1>
  <p class="abs tagline">A live social media integrated portal.</p>

  <section class="features">
    <div class="abs feature-bar" style="left:128px;width:248px">Innovation / Technology</div>
    <div class="abs feature-num" style="left:100px">1</div>
    <p class="abs wrap feature-text" style="left:164px;width:210px">Developments such as mobile devices, mobile internet, video streaming, cloud computing, and web development systems have made it possible for us to develop qulmora with the use of the lastest innovative technologies.</p>

    <div class="abs feature-bar" style="left:420px;width:262px">Social Media, Networking</div>
    <div class="abs feature-num" style="left:391px">2</div>
    <p class="abs wrap feature-text" style="left:460px;width:220px">Users can engage with the event by integrating their existing social networking accounts allowing them to see their connections and establish professional relationships and discussion.</p>

    <div class="abs feature-bar" style="left:724px;width:238px">Live Video Streaming</div>
    <div class="abs feature-num" style="left:694px">3</div>
    <p class="abs wrap feature-text" style="left:756px;width:206px">High quality live video streaming means you get to see the event as it happens without waiting for a stream to buffer. qulmora offers a choice of different resolutions to suit your connection speed.</p>
  </section>

  <div class="abs divider"></div>

  <section class="categories">
    <div class="abs badge badge-edu">Edu</div>
    <div class="abs badge badge-sport">Sport</div>
    <div class="abs badge badge-comms">Comms</div>
    <div class="abs badge badge-gig">Gig</div>

    <h2 class="abs category-title" style="left:137px">Education</h2>
    <p class="abs wrap category-text" style="left:137px;width:180px">With much of todays learning being based off campus, qulmora is an effective educational tool.</p>
    <h2 class="abs category-title" style="left:343px">Sport</h2>
    <p class="abs wrap category-text" style="left:343px;width:175px">View live sports events, check out the stats, and chat with friends about the game.</p>
    <h2 class="abs category-title" style="left:548px">Communications</h2>
    <p class="abs wrap category-text" style="left:548px;width:215px">qulmora is a great communication tool for business with broadcast, discussion and feedback systems built in.</p>
    <h2 class="abs category-title" style="left:786px">Gigs &amp; Festivals</h2>
    <p class="abs wrap category-text" style="left:786px;width:175px">What to see a band but its sold out, watch it live online, while chatting with your friends.</p>
  </section>

  <footer>
    <div class="abs footer-links"></div>
    <div class="abs footer-col" style="left:157px"><h3>INTERESTING LINKS</h3><ul><li>link one goes here</li><li>link two goes here</li><li>link three goes here</li></ul></div>
    <div class="abs footer-col" style="left:362px"><h3>PAGES</h3><ul><li>Education</li><li>Sports</li><li>lCommunications</li></ul></div>
    <div class="abs footer-col" style="left:568px"><h3>CATEGORIES</h3><ul><li>link one goes here</li><li>link two goes here</li><li>link three goes here</li></ul></div>
    <div class="abs footer-col" style="left:782px"><h3>ARCHIVE</h3><ul><li>link one goes here</li><li>link two goes here</li><li>link three goes here</li></ul></div>

    <div class="abs footer-bar"></div>
    <div class="abs footer-brand">qulmora</div>
    <nav class="footer-nav">
      <a href="#" style="left:353px">HOME</a>
      <a href="#" style="left:409px">FEATURES</a>
      <a href="#" style="left:492px">APPS</a>
      <a href="#" style="left:547px">TEAM</a>
      <a href="#" style="left:600px">SUPPORT</a>
      <a href="#" style="left:678px">CONTACT</a>
    </nav>
    <a href="#" class="abs social-square" style="left:805px" aria-label="Vorlo">V</a>
    <a href="#" class="abs social-square" style="left:850px" aria-label="Kestrin">K</a>
    <a href="#" class="abs social-square" style="left:896px" aria-label="Rundel">R</a>
  </footer>
</body>
</html>
```